Modern Yoga Studio Timetable and Flyer Design

We have a comprehensive class timetable and we are wanting to a clean modern look for our Spring timetable.

We require a double sided flyer with our class timetable included.
We would prefer an A5 size (postcard) or DL (1/3 A4).

We would like the final flyer to have.
Side A : Yoga image, logo

Fennel Stretch Hall
address: 4/71 Wexcombe Lane, Pelharton
website: fennelstretch.com.au
mobile: 0471 296 814

Side B: Clear easy to read timetable with a break down of class types and website.

We would also like to have a copy of the timetable itself as a separate jpg or pdf for use on our website to download.

Thank you.
Yours kindly,
Nell

I have attached a sample of another timetable of which I like the look and feel of, however this is just a guide. I've also attached our 'new' schedule in WORD plus uploaded our last design of the front.
Updates

Target Market(s)

Women aged 30-45

Industry/Entity Type

Health And Wellness

Font styles to use
Other font styles liked:
• Brandon Grotesque, Jenna Sue

Colors
6c459b
33a6d7
ffffff

Requirements
Must have
• A definitive colour to decipher between different class types on our timetable. Where each colour represents a different class type. Colours and layouts similar to our website design, see www.fennelstretch.com.au
Nice to have
• I've included a design of another studio whose timetable design I like. One of our own yoga images instead of a stock image.
Should not have
• No dark gridlines between the cells/boxes in the timetables. Please don't use stock yoga images.

```html
<!DOCTYPE html>
<html lang="en">
<head>
<meta charset="utf-8">
<title>Fennel Stretch Hall – Spring Flyer</title>
<link rel="stylesheet" href="https://fonts.googleapis.com/css2?family=Arimo:wght@400;700&family=Caveat:wght@400;500&display=swap">
<style>
  :root{
    --purple:#6c459b;
    --purple-deep:#4f2a7e;
    --purple-soft:#8d6bb8;
    --blue:#33a6d7;
    --blue-bar:#2f7fc8;
    --white:#ffffff;
    --cell:#e6e6e8;
    --ink:#3b2a55;
    --page:#f1f0ee;
    --line:#cfcfd4;
    --skin:#e7b48a;
  }
  *{box-sizing:border-box;margin:0;padding:0}
  html,body{width:984px;height:1200px;overflow:hidden;background:var(--page)}
  body{font-family:"Arimo",Arial,sans-serif;color:var(--ink);position:relative}

  .card{position:absolute;left:92px;width:800px;height:566px;background:var(--white);overflow:hidden;box-shadow:0 2px 10px rgba(0,0,0,.12)}
  .card--front{top:20px}
  .card--back{top:614px}

  /* Front */
  .front-photo{position:absolute;inset:0;background:linear-gradient(180deg,#efeeec 0%,#e6e3df 54%,#b98f63 58%,#a87d52 100%)}
  .front-photo__subject{position:absolute;left:170px;top:20px;width:500px;height:400px;border-radius:50%;
    background:radial-gradient(ellipse at 40% 40%,rgba(108,69,155,.75) 0%,rgba(200,140,110,.55) 45%,rgba(231,180,138,.25) 65%,rgba(231,180,138,0) 75%)}
  .front-wave{position:absolute;left:0;top:0;width:800px;height:566px}
  .brand{position:absolute;left:26px;top:56px;display:flex;align-items:center;gap:10px;color:var(--purple);font-size:22px;letter-spacing:4px}
  .brand__dot{width:16px;height:16px;border-radius:50%;background:var(--purple)}
  .tagline{position:absolute;left:14px;top:150px;width:240px;font-family:"Caveat",cursive;font-size:21px;line-height:1.1;color:var(--purple)}
  .website{position:absolute;right:22px;top:24px;display:flex;align-items:center;gap:8px;font-weight:700;font-size:15px;color:var(--purple)}
  .website__dot{width:12px;height:12px;border-radius:50%;background:var(--purple-soft)}
  .studio-name{position:absolute;right:36px;top:404px;font-family:"Caveat",cursive;font-size:60px;color:var(--white);font-weight:400;white-space:nowrap}
  .phone{position:absolute;left:36px;top:513px;display:flex;align-items:center;gap:8px;color:var(--white);font-weight:700;font-size:28px}
  .address{position:absolute;right:40px;top:520px;display:flex;align-items:center;gap:6px;color:var(--white);font-weight:700;font-size:19px}

  /* Back */
  .timetable-title{position:absolute;left:30px;top:18px;color:var(--purple);font-weight:700;font-size:19px}
  .timetable{position:absolute;left:2px;top:58px;display:grid;grid-template-columns:52px repeat(6,58px);grid-auto-rows:22px;gap:2px;font-size:7.5px}
  .timetable .head{color:var(--white);font-weight:700;font-size:8.5px;display:flex;align-items:center;justify-content:center;height:18px;align-self:end}
  .timetable .head--blue{background:var(--blue)}
  .timetable .head--purple{background:var(--purple)}
  .timetable .time{background:var(--cell);display:flex;align-items:center;padding-left:6px;color:#333}
  .timetable .slot{background:var(--cell);display:flex;align-items:center;padding-left:4px;color:#222;font-weight:700;line-height:1.05;white-space:nowrap}
  .timetable .slot--vinyasa{background:var(--purple);color:var(--white)}
  .timetable .slot--pregnancy{background:var(--blue-bar);color:var(--white)}
  .timetable .slot--family{color:var(--blue)}
  .timetable .slot--plain{background:var(--white)}
  .timetable .slot--wrap{white-space:normal}
  .bookings{position:absolute;left:318px;top:392px;font-size:9px;color:#333}
  .join{position:absolute;left:14px;top:412px;font-weight:700;font-size:22px;color:var(--purple)}
  .join span{color:var(--blue)}
  .contact{position:absolute;top:446px;display:flex;gap:6px;font-size:12px;line-height:1.2;color:#333}
  .contact--studio{left:14px}
  .contact--reach{left:200px;padding-left:14px;border-left:1px solid var(--line)}
  .contact--reach p{display:flex;align-items:center;gap:6px;margin-bottom:4px}
  .follow{position:absolute;left:0;bottom:0;width:392px;height:40px;background:var(--blue-bar);display:flex;align-items:center;justify-content:center;gap:10px;color:var(--white);font-weight:700;font-size:13px}
  .follow__rule{width:1px;height:22px;background:rgba(255,255,255,.6)}
  .follow__mark{width:18px;height:18px;border-radius:50%;background:var(--white)}
  .stamp-box{position:absolute;left:652px;top:26px;width:104px;height:102px;border:1px solid var(--line)}
  .address-line{position:absolute;left:460px;width:240px;height:1px;background:var(--line)}
</style>
</head>
<body>

<section class="card card--front" aria-label="Flyer front">
  <div class="front-photo" role="img" aria-label="Photo of a woman in a purple top and patterned leggings holding downward-facing dog on a mat in a bright studio">
    <div class="front-photo__subject"></div>
  </div>
  <svg class="front-wave" viewBox="0 0 800 566" aria-hidden="true">
    <path d="M0 432 C 180 388 430 352 800 318 L800 566 L0 566 Z" fill="#ffffff"/>
    <path d="M0 456 C 220 402 470 372 800 356 L800 566 L0 566 Z" fill="#6c459b"/>
    <path d="M0 468 C 200 420 330 398 460 392 C 330 410 190 444 0 500 Z" fill="#ffffff"/>
  </svg>
  <div class="brand"><span class="brand__dot"></span>fennel stretch hall</div>
  <p class="tagline">Inclusive,inspiring boutique yoga studio classes for all ages+abilities</p>
  <p class="website"><span class="website__dot"></span>www.fennelstretch.com.au</p>
  <h1 class="studio-name">Fennel Stretch Hall</h1>
  <p class="phone">
    <svg width="24" height="24" viewBox="0 0 24 24" aria-hidden="true"><path fill="#fff" d="M6.6 10.8a15.1 15.1 0 0 0 6.6 6.6l2.2-2.2c.3-.3.7-.4 1-.2 1.1.4 2.3.6 3.6.6.6 0 1 .4 1 1V20c0 .6-.4 1-1 1C10.6 21 3 13.4 3 4c0-.6.4-1 1-1h3.5c.6 0 1 .4 1 1 0 1.3.2 2.5.6 3.6.1.3 0 .7-.2 1z"/></svg>
    0471 296 814
  </p>
  <p class="address">
    <svg width="14" height="18" viewBox="0 0 14 20" aria-hidden="true"><path fill="#fff" d="M7 0a7 7 0 0 0-7 7c0 5 7 13 7 13s7-8 7-13a7 7 0 0 0-7-7zm0 9.5A2.5 2.5 0 1 1 7 4.5a2.5 2.5 0 0 1 0 5z"/></svg>
    4/71 Wexcombe Lane, Pelharton
  </p>
</section>

<section class="card card--back" aria-label="Flyer back">
  <h2 class="timetable-title">FENNEL STRETCH SPRING TIMETABLE</h2>
  <div class="timetable">
    <div></div>
    <div class="head head--blue">MON</div><div class="head head--purple">TUE</div><div class="head head--blue">WED</div><div class="head head--purple">THU</div><div class="head head--blue">FRI</div><div class="head head--purple">SAT</div>

    <div class="time">5:45am</div><div class="slot"></div><div class="slot">Rise+Shine*</div><div class="slot"></div><div class="slot">Rise+Shine*</div><div class="slot"></div><div class="slot"></div>
    <div class="time">9:00am</div><div class="slot"></div><div class="slot"></div><div class="slot"></div><div class="slot"></div><div class="slot"></div><div class="slot slot--vinyasa">Vinyasa Flow</div>
    <div class="time">9:15am</div><div class="slot"></div><div class="slot slot--vinyasa">Vinyasa Flow</div><div class="slot"></div><div class="slot"></div><div class="slot"></div><div class="slot"></div>
    <div class="time">9:30am</div><div class="slot">Slow Flow</div><div class="slot"></div><div class="slot"></div><div class="slot slot--vinyasa">Vinyasa Flow</div><div class="slot"></div><div class="slot"></div>
    <div class="time">10:30am</div><div class="slot"></div><div class="slot"></div><div class="slot"></div><div class="slot"></div><div class="slot"></div><div class="slot slot--pregnancy">Pregnancy*</div>
    <div class="time">11:00am</div><div class="slot"></div><div class="slot slot--family">Mum+Baby*</div><div class="slot"></div><div class="slot slot--family">Mum+Baby*</div><div class="slot"></div><div class="slot"></div>
    <div class="time">12:15pm</div><div class="slot"></div><div class="slot"></div><div class="slot"></div><div class="slot slot--pregnancy">Pregnancy*</div><div class="slot"></div><div class="slot"></div>
    <div class="time">4:00pm</div><div class="slot"></div><div class="slot"></div><div class="slot slot--family">Kids 8-12*</div><div class="slot slot--family">Kids 5-7*</div><div class="slot"></div><div class="slot slot--vinyasa">Vinyasa Flow</div>
    <div class="time">4:45pm</div><div class="slot"></div><div class="slot"></div><div class="slot slot--family">Teens 12-16*</div><div class="slot"></div><div class="slot"></div><div class="slot"></div>
    <div class="time">5:00pm</div><div class="slot"></div><div class="slot"></div><div class="slot"></div><div class="slot slot--family">Teens 12-16*</div><div class="slot"></div><div class="slot"></div>
    <div class="time">6:00pm</div><div class="slot slot--pregnancy">Pregnancy*</div><div class="slot slot--vinyasa">Vinyasa Flow</div><div class="slot">Slow Flow</div><div class="slot"></div><div class="slot slot--plain">Flow + Restore</div><div class="slot"></div>
    <div class="time">6:15pm</div><div class="slot"></div><div class="slot"></div><div class="slot"></div><div class="slot slot--pregnancy">Pregnancy*</div><div class="slot"></div><div class="slot"></div>
    <div class="time">7:30pm</div><div class="slot slot--vinyasa">Vinyasa Flow</div><div class="slot slot--pregnancy">Pregnancy*</div><div class="slot">Yin + Restore</div><div class="slot slot--plain slot--wrap">Women's Wellness*</div><div class="slot"></div><div class="slot"></div>
  </div>
  <p class="bookings">* bookings essential</p>

  <h3 class="join"><span>JOIN</span> A STUDIO CLASS:</h3>
  <div class="contact contact--studio">
    <svg width="10" height="14" viewBox="0 0 14 20" aria-hidden="true"><path fill="#33a6d7" d="M7 0a7 7 0 0 0-7 7c0 5 7 13 7 13s7-8 7-13a7 7 0 0 0-7-7zm0 9.5A2.5 2.5 0 1 1 7 4.5a2.5 2.5 0 0 1 0 5z"/></svg>
    <p>Harrowby Shopping Ctr<br>4/71 WEXCOMBE LANE<br>PELHARTON WA 6087</p>
  </div>
  <div class="contact contact--reach">
    <div>
      <p><svg width="12" height="9" viewBox="0 0 12 9" aria-hidden="true"><rect width="12" height="9" fill="#33a6d7"/><path d="M0 0l6 5 6-5" stroke="#fff" fill="none"/></svg>hello@fennelstretch.com.au</p>
      <p><svg width="12" height="12" viewBox="0 0 24 24" aria-hidden="true"><path fill="#33a6d7" d="M6.6 10.8a15.1 15.1 0 0 0 6.6 6.6l2.2-2.2c.3-.3.7-.4 1-.2 1.1.4 2.3.6 3.6.6.6 0 1 .4 1 1V20c0 .6-.4 1-1 1C10.6 21 3 13.4 3 4c0-.6.4-1 1-1h3.5c.6 0 1 .4 1 1 0 1.3.2 2.5.6 3.6.1.3 0 .7-.2 1z"/></svg>0471 296 814</p>
    </div>
  </div>
  <div class="follow">Follow us on <span class="follow__rule"></span><span class="follow__mark"></span><span class="follow__mark"></span><span class="follow__mark"></span></div>

  <div class="stamp-box"></div>
  <div class="address-line" style="top:356px"></div>
  <div class="address-line" style="top:390px"></div>
  <div class="address-line" style="top:428px"></div>
</section>

</body>
</html>
```